Castlewood Trading Company need a book cover designing. The book is called "Gather M...

Please submit it as a jpg at 300 dpi with A5 dimensions (14.8 cm wide by 21 cm high), and make sure that your text is well within the trim line - approximately 2 cm from the edge. We like the style "Gather" is written in the attached image, although this is a guideline. It CANNOT be copied, but it may provide influence and inspiration. We are looking for a crisp and clean book cover, so probably on a white background.Our Logo is also attached and we see this being included centered at the bottom "There is a better way to grow your savings" is what the book is about

```html
<!DOCTYPE html>
<html lang="en">
<head>
<meta charset="utf-8">
<title>Gather Max — Book Cover</title>
<link rel="stylesheet" href="https://fonts.googleapis.com/css2?family=Kaushan+Script&family=Oswald:wght@300;500&display=swap">
<style>
  :root {
    --paper: #ffffff;
    --ink-navy: #1b1f44;
    --ink-soft: #2a2a2a;
    --leaf-green: #7dc242;
    --coin-gold: #b59a45;
    --coin-light: #ddc98a;
    --shoot-green: #6f9a3a;
  }
  * { margin: 0; padding: 0; box-sizing: border-box; }
  html, body {
    width: 906px;
    height: 1200px;
    overflow: hidden;
    background: var(--paper);
  }
  .book-cover {
    position: relative;
    width: 906px;
    height: 1200px;
    background: var(--paper);
  }
  .cover-title {
    position: absolute;
    top: 250px;
    left: 0;
    width: 100%;
    text-align: center;
    font-family: "Kaushan Script", cursive;
    font-weight: 400;
    font-size: 150px;
    line-height: 1;
    color: var(--ink-navy);
    letter-spacing: 2px;
  }
  .title-rule {
    position: absolute;
    top: 462px;
    left: 163px;
    width: 580px;
    height: 3px;
    background: var(--leaf-green);
  }
  .cover-subtitle {
    position: absolute;
    top: 482px;
    left: 0;
    width: 100%;
    text-align: center;
    font-family: "Oswald", sans-serif;
    font-weight: 300;
    font-size: 40px;
    color: var(--ink-soft);
  }
  .savings-visual {
    position: absolute;
    top: 600px;
    left: 110px;
    width: 686px;
    height: 420px;
    border-radius: 8px;
    background:
      radial-gradient(ellipse 70% 28% at 50% 88%, var(--coin-light) 0%, var(--coin-gold) 55%, rgba(181,154,69,0) 100%),
      linear-gradient(180deg, rgba(111,154,58,0.35) 0%, rgba(111,154,58,0.15) 45%, rgba(255,255,255,0) 75%);
  }
  .brand-mark {
    position: absolute;
    top: 1070px;
    left: 0;
    width: 100%;
    display: flex;
    justify-content: center;
    align-items: center;
    gap: 18px;
  }
  .brand-dot {
    width: 58px;
    height: 58px;
    border-radius: 50%;
    background: var(--ink-navy);
  }
  .brand-name {
    font-family: "Oswald", sans-serif;
    font-weight: 500;
    font-size: 52px;
    letter-spacing: 4px;
    color: var(--ink-navy);
    line-height: 1;
  }
</style>
</head>
<body>
  <main class="book-cover">
    <h1 class="cover-title">Gather Max</h1>
    <div class="title-rule"></div>
    <p class="cover-subtitle">There is a better way to grow your savings</p>
    <div class="savings-visual" role="img" aria-label="Photograph of young green seedlings sprouting from rolled dollar, pound and euro banknotes standing on a pile of gold coins"></div>
    <div class="brand-mark">
      <span class="brand-dot"></span>
      <span class="brand-name">GATHER MAX</span>
    </div>
  </main>
</body>
</html>
```